Brivanta.com the Free Online Tutorial Needs a New Web Design

We need a new web design for our existing website, Brivanta.com. We provide a Free Online Tutorial of any code, like HTML, CSS, PHP, Jquery, javascript etc, including online editor.
We would like to see designs that interesting, simple, interactive, and be a very comfortable place to read in a long time.
We need 2 pages design for:
1. Home Page (http://brivanta.com) and
2. Listing Page (http://brivanta.com/tutorial/833/sql/sql-basics/sql-and-or-operator.html)
For Listing Page We need nice "Left Menu" at left side and Content Page (min 728px) at right side.
I need File PSD and/or Vector Only, without HTML code.
Online
2 page

```html
<!DOCTYPE html>
<html lang="en">
<head>
<meta charset="utf-8">
<title>Brivanta – SQL And / Or</title>
<link rel="stylesheet" href="https://fonts.googleapis.com/css2?family=Open+Sans:wght@400;600&display=swap">
<style>
:root{
  --dark:#222222;
  --dark-2:#2b2b2b;
  --line-dark:#3a3a3a;
  --white:#ffffff;
  --ink:#222222;
  --ink-soft:#444444;
  --muted:#b5b5b5;
  --muted-2:#8a8a8a;
  --row-alt:#f2f2f2;
  --grid:#dddddd;
  --input:#1a1a1a;
  --blue:#1e7fd6;
  --green:#5cb845;
  --yellow:#f2d22e;
  --red:#e8433a;
  --orange:#f7a21b;
  --circle:#555555;
}
*{margin:0;padding:0;box-sizing:border-box}
html,body{width:672px;height:1200px;overflow:hidden;background:var(--white)}
body{position:relative;font-family:"Open Sans",Arial,sans-serif;color:var(--ink)}
ul{list-style:none}

/* top bar */
.topbar{position:absolute;left:0;top:0;width:672px;height:34px;background:var(--dark)}
.brand{position:absolute;left:120px;top:8px;display:flex;align-items:center;gap:5px;color:var(--white);font-size:14px;font-weight:400;line-height:18px}
.brand-mark{width:14px;height:14px;background:var(--orange)}
.login-label{position:absolute;left:228px;top:13px;font-size:6px;color:var(--muted);letter-spacing:.2px}
.login-input{position:absolute;top:9px;width:76px;height:17px;background:var(--input);border:1px solid var(--line-dark)}
.login-input.user{left:268px}
.login-input.pass{left:350px;width:75px}
.login-btn{position:absolute;left:430px;top:9px;width:45px;height:17px;background:var(--input);border:1px solid var(--line-dark);color:var(--white);font-size:6.5px;text-align:center;line-height:15px}
.signup-btn{position:absolute;left:492px;top:9px;width:84px;height:17px;background:linear-gradient(90deg,var(--blue),var(--green) 35%,var(--yellow) 55%,var(--red) 80%,var(--orange));color:var(--white);font-size:5.6px;font-weight:600;text-align:center;line-height:17px}

/* sidebar */
.sidebar{position:absolute;left:110px;top:34px;width:111px;height:1166px;background:var(--dark);color:var(--muted)}
.tagline{position:absolute;left:6px;top:4px;width:100px;font-size:6px;line-height:8px;color:var(--white)}
.main-nav{position:absolute;left:0;top:30px;width:106px}
.main-nav li{height:14.4px;border-bottom:1px solid var(--line-dark);font-size:6.3px;color:var(--white);line-height:14px;padding-left:5px;display:flex;align-items:center;gap:5px}
.main-nav svg{width:6px;height:6px}
.tryit-btn{position:absolute;left:18px;top:166px;width:63px;height:22px;border:1px solid #555;background:var(--dark-2);color:var(--white);font-size:6px;text-align:center;line-height:20px}
.topic{position:absolute;left:4px}
.topic h3{font-size:7px;font-weight:400;color:var(--white);line-height:9px}
.topic li{font-size:5px;line-height:6.85px;color:var(--muted);white-space:nowrap}
.connect{position:absolute;left:1px;top:807px;font-size:7.4px;color:var(--white);letter-spacing:.4px}
.social{position:absolute;top:826px;width:24px;height:24px;border-radius:50%;background:var(--circle)}
.social.one{left:1px}.social.two{left:28px}
.site-links{position:absolute;left:6px;top:872px}
.site-links li{font-size:5.6px;line-height:11.7px;color:var(--muted-2)}

/* content */
.content{position:absolute;left:228px;top:34px;width:350px}
.page-title{position:absolute;left:2px;top:12px;font-size:11px;font-weight:400}
.intro{position:absolute;left:1px;top:30px;font-size:4.9px;line-height:8px;color:var(--ink-soft)}
.example{position:absolute;left:0;width:350px}
.example h2{font-size:10.5px;font-weight:400;line-height:14px}
.example .lead{font-size:5.3px;color:var(--ink-soft);margin-top:0}
.try-now{position:absolute;right:1px;top:-2px;width:56px;height:16px;background:var(--dark);color:var(--white);font-size:7.2px;text-align:center;line-height:16px}
.buyers{position:absolute;left:0;top:22px;width:350px;border-collapse:collapse;table-layout:fixed}
.buyers th{height:17px;background:transparent;color:var(--white);font-size:7px;font-weight:400;text-align:center}
.buyers thead tr{background:linear-gradient(90deg,var(--blue) 0%,var(--blue) 15%,var(--green) 38%,var(--yellow) 55%,var(--red) 70%,var(--orange) 100%)}
.buyers td{height:14px;font-size:6.3px;padding-left:4px;border:1px solid var(--grid);white-space:nowrap;overflow:hidden;color:var(--ink-soft)}
.buyers tbody tr:nth-child(even){background:var(--row-alt)}
.c-id{width:40px}.c-name{width:65px}.c-addr{width:93px}.c-city{width:64px}.c-country{width:46px}.c-dep{width:42px}

.random{position:absolute}
.random h4{font-size:7px;font-weight:400;line-height:9px}
.random li{font-size:5.3px;line-height:7.7px;color:var(--ink-soft);white-space:nowrap}
</style>
</head>
<body>

<header class="topbar">
  <div class="brand"><span class="brand-mark"></span>Brivanta</div>
  <span class="login-label">LOGIN HERE</span>
  <div class="login-input user"></div>
  <div class="login-input pass"></div>
  <div class="login-btn">Login</div>
  <div class="signup-btn">NEW USER? SIGN UP HERE</div>
</header>

<aside class="sidebar">
  <p class="tagline">The Free Online Tutorials Place Brivanta</p>
  <ul class="main-nav">
    <li><svg viewBox="0 0 6 6"><path d="M0.5 3.2 2.3 5 5.5 1" stroke="#fff" stroke-width="1.2" fill="none"/></svg>HOME</li>
    <li><svg viewBox="0 0 6 6"><path d="M0.5 3.2 2.3 5 5.5 1" stroke="#fff" stroke-width="1.2" fill="none"/></svg>HTML</li>
    <li><svg viewBox="0 0 6 6"><path d="M0.5 3.2 2.3 5 5.5 1" stroke="#fff" stroke-width="1.2" fill="none"/></svg>CSS</li>
    <li><svg viewBox="0 0 6 6"><path d="M0.5 3.2 2.3 5 5.5 1" stroke="#fff" stroke-width="1.2" fill="none"/></svg>JAVASCRIPT</li>
    <li><svg viewBox="0 0 6 6"><path d="M0.5 3.2 2.3 5 5.5 1" stroke="#fff" stroke-width="1.2" fill="none"/></svg>PHP</li>
    <li><svg viewBox="0 0 6 6"><path d="M0.5 3.2 2.3 5 5.5 1" stroke="#fff" stroke-width="1.2" fill="none"/></svg>SQL</li>
    <li><svg viewBox="0 0 6 6"><path d="M0.5 3.2 2.3 5 5.5 1" stroke="#fff" stroke-width="1.2" fill="none"/></svg>JQUERY</li>
    <li><svg viewBox="0 0 6 6"><path d="M0.5 3.2 2.3 5 5.5 1" stroke="#fff" stroke-width="1.2" fill="none"/></svg>JSON</li>
    <li><svg viewBox="0 0 6 6"><path d="M0.5 3.2 2.3 5 5.5 1" stroke="#fff" stroke-width="1.2" fill="none"/></svg>MORE...</li>
  </ul>
  <div class="tryit-btn">Tryit Yourself</div>

  <section class="topic" style="top:200px">
    <h3>SQL Syntax</h3>
    <ul><li>SQL Data Types (Access)</li><li>SQL Data Types (MySQL)</li><li>SQL Data Types (Oracle)</li><li>SQL Data Types (SQL Server)</li><li>SQL Reference</li><li>SQL TerminologySQL Introduction</li><li>SQL Syntax</li><li>SQL Data Types (Access)</li><li>SQL Data Types (MySQL)</li><li>SQL Data Types (Oracle)</li><li>SQL Data Types (SQL Server)</li><li>SQL Reference</li><li>SQL Terminology</li></ul>
  </section>
  <section class="topic" style="top:305px">
    <h3>SQL Basics</h3>
    <ul><li>SQL And / Or</li><li>SQL DELETE</li><li>SQL DISTINCT</li><li>SQL Group By</li><li>SQL Insert</li><li>SQL Not</li><li>SQL Order By</li><li>SQL Select</li><li>SQL Update</li><li>SQL Where</li><li>SQL Create Database</li><li>SQL Create Table</li><li>SQL Drop</li><li>SQL TRUNCATE</li></ul>
  </section>
  <section class="topic" style="top:415px">
    <h3>SQL Advanced</h3>
    <ul><li>SQL And / Or</li><li>SQL Alias</li><li>SQL Alter</li><li>SQL Auto-increment</li><li>SQL Between</li><li>SQL Create Index</li><li>SQL In</li><li>SQL IsnullI()</li><li>SQL Like</li><li>SQL Null Values</li><li>SQL Select Into</li><li>SQL Union</li><li>SQL Top</li><li>SQL View</li></ul>
  </section>
  <section class="topic" style="top:526px">
    <h3>SQL Constraints</h3>
    <ul><li>SQL Constraints Overview</li><li>SQL Check</li><li>SQL Default</li><li>SQL Not Null</li><li>SQL Primary Key</li><li>SQL Foreign Key</li><li>SQL UniqueSQL Constraints Overview</li><li>SQL Check</li><li>SQL Default</li><li>SQL Not Null</li><li>SQL Primary Key</li><li>SQL Foreign Key</li><li>SQL Unique</li></ul>
  </section>
  <section class="topic" style="top:630px">
    <h3>SQL Joins</h3>
    <ul><li>SQL Joins Overview</li><li>SQL Full</li><li>SQL Inner Join</li><li>SQL Left Join</li><li>SQL Right Join</li></ul>
  </section>
  <section class="topic" style="top:679px">
    <h3>SQL Functions</h3>
    <ul><li>SQL Functions Overview</li><li>SQL AVG()</li><li>SQL COUNT()</li><li>SQL FIRST()</li><li>SQL FORMAT()</li><li>SQL LAST()</li><li>SQL LCASE() / LOWER()</li><li>SQL LEN()</li><li>SQL MAX()</li><li>SQL MID()</li><li>SQL MIN()</li><li>SQL NOW()</li><li>SQL ROUND()</li><li>SQL SUM()</li><li>SQL UCASE() / UPPER()</li></ul>
  </section>

  <p class="connect">CONNECT TO US ON</p>
  <span class="social one"></span>
  <span class="social two"></span>
  <ul class="site-links">
    <li>Tutorial</li><li>Articles</li><li>Try it</li><li>Canvas</li><li>Webtools</li><li>About</li><li>Terms</li><li>Privacy</li><li>Disclaimer</li><li>Contact</li><li>FAQ</li><li>Find Us on Friendloop</li><li>Brivanta © 2015, All rights reserved</li>
  </ul>
</aside>

<main class="content">
  <h1 class="page-title">SQL And / Or</h1>
  <p class="intro">The AND &amp; OR operators are used to filter records based on more than one condition.<br>The AND operator displays a record if both the first condition and the second condition is true.<br>The OR operator displays a record if either the first condition or the second condition is true.</p>

  <section class="example" style="top:66px">
    <h2>Example with AND Operator</h2>
    <p class="lead">Consider the following "Buyers" table:</p>
    <span class="try-now">Try it now</span>
    <table class="buyers">
      <thead><tr><th class="c-id">BuyerID</th><th class="c-name">BuyerName</th><th class="c-addr">BuyerAddress</th><th class="c-city">City</th><th class="c-country">Country</th><th class="c-dep">Deposit</th></tr></thead>
      <tbody>
        <tr><td>1</td><td>David Clinton</td><td>Blue Lake 123</td><td>New York</td><td>USA</td><td>435.45</td></tr>
        <tr><td>2</td><td>Shea Roxanne</td><td>Santa Rose 123</td><td>Liverpool</td><td>England</td><td>234.12</td></tr>
        <tr><td>3</td><td>Bryan de Lima</td><td>Corcovado Street</td><td>Rio de Janeiro</td><td>Brazil</td><td>534.22</td></tr>
        <tr><td>4</td><td>Tjen Chun Yen</td><td>Zhonghua Street 456</td><td>Shanghai</td><td>China</td><td>234.12</td></tr>
        <tr><td>5</td><td>Sheila White</td><td>Santa San Marine 456</td><td>New York</td><td>USA</td><td>234.12</td></tr>
        <tr><td>6</td><td>Bryan Clinton</td><td>Blue Lake 123</td><td>Sidney</td><td>Australia</td><td>534.22</td></tr>
        <tr><td>7</td><td>David Clinton</td><td>Blue Lake 123</td><td>Sidney</td><td>Australia</td><td>4361.87</td></tr>
        <tr><td>8</td><td>Tjen Chun Yen</td><td>Blue Lake 123</td><td>Singapore City</td><td>Singapore</td><td>308.33</td></tr>
        <tr><td>9</td><td>Sheila White</td><td>Santa San Marine 456</td><td>Sidney</td><td>Australia</td><td>435.45</td></tr>
      </tbody>
    </table>
  </section>

  <section class="example" style="top:249px">
    <h2>Example with AND Operator</h2>
    <p class="lead">Consider the following "Buyers" table:</p>
    <span class="try-now">Try it now</span>
    <table class="buyers">
      <thead><tr><th class="c-id">BuyerID</th><th class="c-name">BuyerName</th><th class="c-addr">BuyerAddress</th><th class="c-city">City</th><th class="c-country">Country</th><th class="c-dep">Deposit</th></tr></thead>
      <tbody>
        <tr><td>1</td><td>David Clinton</td><td>Blue Lake 123</td><td>New York</td><td>USA</td><td>435.45</td></tr>
        <tr><td>2</td><td>Shea Roxanne</td><td>Santa Rose 123</td><td>Liverpool</td><td>England</td><td>234.12</td></tr>
        <tr><td>3</td><td>Bryan de Lima</td><td>Corcovado Street</td><td>Rio de Janeiro</td><td>Brazil</td><td>534.22</td></tr>
        <tr><td>4</td><td>Tjen Chun Yen</td><td>Zhonghua Street 456</td><td>Shanghai</td><td>China</td><td>234.12</td></tr>
        <tr><td>5</td><td>Sheila White</td><td>Santa San Marine 456</td><td>New York</td><td>USA</td><td>234.12</td></tr>
        <tr><td>6</td><td>Bryan Clinton</td><td>Blue Lake 123</td><td>Sidney</td><td>Australia</td><td>534.22</td></tr>
        <tr><td>7</td><td>David Clinton</td><td>Blue Lake 123</td><td>Sidney</td><td>Australia</td><td>4361.87</td></tr>
        <tr><td>8</td><td>Tjen Chun Yen</td><td>Blue Lake 123</td><td>Singapore City</td><td>Singapore</td><td>308.33</td></tr>
        <tr><td>9</td><td>Sheila White</td><td>Santa San Marine 456</td><td>Sidney</td><td>Australia</td><td>435.45</td></tr>
      </tbody>
    </table>
  </section>

  <section class="example" style="top:440px">
    <h2>Example with AND Operator</h2>
    <p class="lead">Consider the following "Buyers" table:</p>
    <span class="try-now">Try it now</span>
    <table class="buyers">
      <thead><tr><th class="c-id">BuyerID</th><th class="c-name">BuyerName</th><th class="c-addr">BuyerAddress</th><th class="c-city">City</th><th class="c-country">Country</th><th class="c-dep">Deposit</th></tr></thead>
      <tbody>
        <tr><td>1</td><td>David Clinton</td><td>Blue Lake 123</td><td>New York</td><td>USA</td><td>435.45</td></tr>
        <tr><td>2</td><td>Shea Roxanne</td><td>Santa Rose 123</td><td>Liverpool</td><td>England</td><td>234.12</td></tr>
        <tr><td>3</td><td>Bryan de Lima</td><td>Corcovado Street</td><td>Rio de Janeiro</td><td>Brazil</td><td>534.22</td></tr>
        <tr><td>4</td><td>Tjen Chun Yen</td><td>Zhonghua Street 456</td><td>Shanghai</td><td>China</td><td>234.12</td></tr>
        <tr><td>5</td><td>Sheila White</td><td>Santa San Marine 456</td><td>New York</td><td>USA</td><td>234.12</td></tr>
        <tr><td>6</td><td>Bryan Clinton</td><td>Blue Lake 123</td><td>Sidney</td><td>Australia</td><td>534.22</td></tr>
        <tr><td>7</td><td>David Clinton</td><td>Blue Lake 123</td><td>Sidney</td><td>Australia</td><td>4361.87</td></tr>
        <tr><td>8</td><td>Tjen Chun Yen</td><td>Blue Lake 123</td><td>Singapore City</td><td>Singapore</td><td>308.33</td></tr>
        <tr><td>9</td><td>Sheila White</td><td>Santa San Marine 456</td><td>Sidney</td><td>Australia</td><td>435.45</td></tr>
        <tr><td>1</td><td>David Clinton</td><td>Blue Lake 123</td><td>New York</td><td>USA</td><td>435.45</td></tr>
        <tr><td>2</td><td>Shea Roxanne</td><td>Santa Rose 123</td><td>Liverpool</td><td>England</td><td>234.12</td></tr>
        <tr><td>3</td><td>Bryan de Lima</td><td>Corcovado Street</td><td>Rio de Janeiro</td><td>Brazil</td><td>534.22</td></tr>
        <tr><td>4</td><td>Tjen Chun Yen</td><td>Zhonghua Street 456</td><td>Shanghai</td><td>China</td><td>234.12</td></tr>
        <tr><td>5</td><td>Sheila White</td><td>Santa San Marine 456</td><td>New York</td><td>USA</td><td>234.12</td></tr>
        <tr><td>6</td><td>Bryan Clinton</td><td>Blue Lake 123</td><td>Sidney</td><td>Australia</td><td>534.22</td></tr>
        <tr><td>7</td><td>David Clinton</td><td>Blue Lake 123</td><td>Sidney</td><td>Australia</td><td>4361.87</td></tr>
        <tr><td>8</td><td>Tjen Chun Yen</td><td>Blue Lake 123</td><td>Singapore City</td><td>Singapore</td><td>308.33</td></tr>
        <tr><td>9</td><td>Sheila White</td><td>Santa San Marine 456</td><td>Sidney</td><td>Australia</td><td>435.45</td></tr>
      </tbody>
    </table>
  </section>

  <section class="random" style="left:10px;top:807px">
    <h4>Random Javascript</h4>
    <ul><li>Javascript Looping</li><li>JS String-HTML italics()</li><li>JS DOM Input FileUpload</li><li>JS Global encodeURI()</li><li>JS Number valueOf()</li><li>JS Math pow(x,y)</li><li>Javascript Array Concat()</li><li>JS Number toExponential()</li><li>JS DOM Meta</li><li>JS Number Positive_Infini..</li></ul>
  </section>
  <section class="random" style="left:142px;top:807px">
    <h4>Random HTML5</h4>
    <ul><li>sup tag in html5</li><li>Geolocation</li><li>img html5</li><li>p in html5</li><li>Button Tag is used to def..</li><li>textarea html5</li><li>Text Formating Overview i..</li><li>h5 in html5</li><li>menu html5</li><li>List Overview html5</li></ul>
  </section>
  <section class="random" style="left:247px;top:805px">
    <h4>Random Articles</h4>
    <ul><li>How to make WHOIS lookups..</li><li>How to Auto Select All Te..</li><li>How to Make SQL Syntax Hi..</li><li>Changing text with innerh..</li><li>How to Make Drop Down Men..</li><li>Create Transparency Anima..</li><li>Make A Lot of Circle Anim..</li><li>How to get an input text ..</li><li>How to Make Drop Down Men..</li><li>How to Make Sitemap.xml</li></ul>
  </section>
  <section class="random" style="left:10px;top:922px">
    <h4>Random Try it</h4>
    <ul><li>Heading with CSS styled</li><li>Colors RGB in HTML</li><li>aside tag example</li><li>tt tag example</li><li>br tag example</li><li>title tag example</li><li>Entities and Symbol HTML</li><li>rp tag example</li><li>datalist tag example</li><li>canvas draw gradient exam..</li></ul>
  </section>
  <section class="random" style="left:142px;top:922px">
    <h4>Random Canvas</h4>
    <ul><li>Canvas Polyline</li><li>Canvas Radial Gradient</li><li>Canvas Draw Images</li><li>Canvas Arc</li><li>Canvas Line</li><li>Canvas Semicircles</li><li>Canvas Line Cap</li><li>Canvas Introduction</li><li>Canvas Bezier Curve</li><li>Canvas Line Width</li></ul>
  </section>
</main>

</body>
</html>
```